Website Design, Ecommerce, Device Buyback, Four concepct pages

Full website design, concept and select pages.
* Home page
* Device catalog
* Order Summary

Require all design assets:
+ static images
+ color pallettes
+ fonts
Would prefer 'atomic' design elements.

Current concept site: http://vlmr.webnestly.example/
Updates

Need extra days to review

Target Market(s)

us retail

Industry/Entity Type

Ecommerce

Number of Pages Required

3 page

Font styles to use
Serif
Sans Serif

Requirements
Must have
• * Home page
* Device catalog
* Order Summary
* Informational page

+ static images
+ color pallettes
+ fonts
Nice to have
• Would prefer 'atomic' design elements.
Additional pages nice to have:
* Form pages, eg contact form, login form
* Reviews page
* Back office pages: user management, catalog management, order management, etc.

```html
<!DOCTYPE html>
<html lang="en">
<head>
<meta charset="utf-8">
<title>TradeLoop – Buy Back</title>
<link href="https://fonts.googleapis.com/css2?family=Poppins:wght@300;400;500;600;700;800&display=swap" rel="stylesheet">
<style>
:root{
  --navy:#0d1e4c;
  --ink:#222631;
  --muted:#6b6f7b;
  --hero-bg:#f6f6fa;
  --card-bg:#f2f2f7;
  --red:#ff2d0a;
  --blue:#1a7fe8;
  --green:#22b01c;
  --about-bg:#02305c;
  --about-text:#9cb8dc;
  --footer-bg:#1c1e2c;
  --footer-text:#8a8d99;
  --white:#ffffff;
}
*{margin:0;padding:0;box-sizing:border-box}
html,body{width:1200px;height:2586px;overflow:hidden}
body{font-family:'Poppins',sans-serif;color:var(--ink);background:var(--white)}
.page{position:relative;width:1200px;height:2586px;overflow:hidden}
.abs{position:absolute}

/* hero */
.hero{position:absolute;left:0;top:0;width:1200px;height:720px;background:var(--hero-bg)}
.hero-photo{position:absolute;left:0;top:0}
.hero-art{position:absolute;left:637px;top:203px;width:374px;height:350px;border-radius:26px 26px 10px 10px;background:linear-gradient(180deg,#8aa8d6 0%,#4d6fa3 55%,#123a6c 100%);opacity:.92}
.hero-wave{position:absolute;left:0;top:0}
.brand{position:absolute;left:150px;top:24px;display:flex;align-items:center;gap:10px;font-weight:700;font-size:28px;color:var(--red);letter-spacing:-.5px}
.brand-dot{width:18px;height:18px;border-radius:50%;background:var(--red)}
.nav{position:absolute;top:32px;left:595px;display:flex;gap:40px;font-size:14px;font-weight:500;color:var(--white)}
.login{position:absolute;left:949px;top:25px;width:90px;height:32px;border-radius:16px;background:var(--white);color:var(--navy);font-size:14px;font-weight:500;display:flex;align-items:center;justify-content:center}
.hero-title{position:absolute;left:159px;top:218px;font-size:38px;line-height:48px;font-weight:800;color:var(--navy)}
.hero-copy{position:absolute;left:159px;top:332px;width:380px;font-size:15.5px;line-height:27px;color:#3a3d48}
.btn{position:absolute;border-radius:22px;display:flex;align-items:center;justify-content:center;font-size:13px;font-weight:500}
.btn-red{background:var(--red);color:var(--white)}
.btn-quote{left:159px;top:430px;width:132px;height:41px}
.btn-ghost{left:307px;top:430px;width:148px;height:41px;background:#e8f1f9;border:1px solid #c7dbef;color:var(--navy);gap:14px}

/* buy back */
.section-title{position:absolute;left:0;width:1200px;text-align:center}
.bb-title{top:751px;font-size:21px;font-weight:700;color:var(--ink)}
.bb-sub{top:790px;font-size:11.5px;color:#4a4d57}
.card{position:absolute;top:898px;width:299px;height:308px;background:var(--card-bg);border-radius:3px}
.card-phone{left:290px}
.card-tablet{left:621px}
.device{position:absolute;border-radius:18px}
.device-phone{left:405px;top:846px;width:102px;height:214px;background:linear-gradient(110deg,#1d2230 0%,#3c4a6a 45%,#e8e9ee 55%,#fafafa 100%)}
.device-tablet{left:712px;top:850px;width:144px;height:210px;border-radius:12px;background:linear-gradient(120deg,#22242b 0%,#2c7fd1 30%,#59b6ec 50%,#c9ccd2 70%,#e4e6ea 100%)}
.card-text{position:absolute;top:1079px;width:299px;text-align:center;font-size:12.5px;line-height:20px;color:#3a3d48}
.btn-browse{top:1137px;width:109px;height:34px;font-size:12px;font-weight:600}

/* how it works */
.hiw-title{top:1344px;font-size:33px;font-weight:400;color:var(--ink)}
.hiw-title b{font-weight:700;color:var(--navy)}
.hiw-sub{top:1397px;font-size:13.5px;line-height:24px;color:var(--muted)}
.step-icon{position:absolute;top:1492px;width:75px;height:75px;border-radius:50%;display:flex;align-items:center;justify-content:center}
.step-title{position:absolute;top:1588px;width:300px;text-align:center;font-size:20px;font-weight:500;color:var(--ink)}
.step-text{position:absolute;top:1625px;width:300px;text-align:center;font-size:13.5px;line-height:23px;color:var(--muted)}

/* about */
.about{position:absolute;left:0;top:1823px;width:1200px;height:460px;background:var(--about-bg)}
.about-art{position:absolute;left:235px;top:110px;width:272px;height:244px;border-radius:18px;background:linear-gradient(180deg,rgba(255,255,255,.22),rgba(255,255,255,.08))}
.about-title{position:absolute;left:568px;top:115px;font-size:37px;font-weight:400;color:var(--white)}
.about-title b{font-weight:700}
.about-copy{position:absolute;left:568px;top:188px;width:440px;font-size:15.5px;line-height:26.5px;color:var(--about-text)}

/* footer */
.footer{position:absolute;left:0;top:2283px;width:1200px;height:303px;background:var(--footer-bg)}
.footer-brand{position:absolute;left:0;top:38px;width:1200px;display:flex;justify-content:center;align-items:center;gap:10px;font-size:28px;font-weight:700;color:var(--white)}
.footer-brand .brand-dot{background:var(--white)}
.footer-nav{position:absolute;top:115px;left:0;width:1200px;display:flex;justify-content:center;gap:36px;font-size:13px;color:var(--footer-text)}
.social{position:absolute;top:2443px;width:34px;height:34px;border-radius:50%;background:#262938}
.social.active{background:#0a3a6e}
.legal{position:absolute;top:2541px;font-size:11px;color:var(--footer-text)}
</style>
</head>
<body>
<div class="page">

  <header class="hero">
    <svg class="hero-photo" width="1200" height="720" role="img" aria-label="Photo of a smiling young woman using a smartphone, in deep blue tones">
      <defs>
        <linearGradient id="photoTone" x1="0" y1="0" x2="1" y2="1">
          <stop offset="0" stop-color="#1b3f72"/>
          <stop offset=".5" stop-color="#2e5d93"/>
          <stop offset="1" stop-color="#12305a"/>
        </linearGradient>
      </defs>
      <path d="M355 0 C420 110 520 205 640 222 C760 238 840 300 900 400 C960 500 1010 610 1200 628 L1200 0 Z" fill="#e4e6ee"/>
      <path d="M382 0 C440 100 530 192 650 205 C770 218 850 285 905 385 C960 485 1010 585 1200 602 L1200 0 Z" fill="url(#photoTone)"/>
    </svg>
    <div class="hero-art" role="img" aria-label="Illustration of a monitor holding a tablet and phone with a check mark"></div>
    <svg class="hero-wave" width="1200" height="720" aria-hidden="true">
      <path d="M0 640 C250 615 450 635 650 670 C820 700 1000 690 1200 645 L1200 720 L0 720 Z" fill="#ffffff"/>
    </svg>

    <div class="brand"><span class="brand-dot"></span>TradeLoop</div>
    <nav class="nav"><span>Home</span><span>Phones</span><span>Tablets</span><span>Contact</span></nav>
    <div class="login">Login</div>

    <h1 class="hero-title">Buy Back<br>Get a Quote, Get Paid</h1>
    <p class="hero-copy">We are a leading company in the industry of computer and phone repairs throughout Florida.</p>
    <div class="btn btn-red btn-quote">Get a Quote</div>
    <div class="btn btn-ghost">
      <svg width="16" height="16" viewBox="0 0 16 16" aria-hidden="true"><circle cx="8" cy="8" r="8" fill="#0d1e4c"/><path d="M6.3 4.8 L11 8 L6.3 11.2 Z" fill="#fff"/></svg>
      Browse All
    </div>
  </header>

  <section class="buy-back">
    <h2 class="section-title bb-title">Buy Back</h2>
    <p class="section-title bb-sub">Bring your device into any one of our convenient locations.</p>

    <div class="card card-phone">
      <p class="card-text" style="top:181px">All kinds of phones including<br>smartphones</p>
      <div class="btn btn-red btn-browse" style="left:95px;top:239px">Browse</div>
    </div>
    <div class="card card-tablet">
      <p class="card-text" style="top:181px">All kinds of tablets</p>
      <div class="btn btn-red btn-browse" style="left:95px;top:239px">Browse</div>
    </div>
    <div class="device device-phone" role="img" aria-label="Product photo of a smartphone, front and back"></div>
    <div class="device device-tablet" role="img" aria-label="Product photo of a tablet, front and back"></div>
  </section>

  <section class="how">
    <h2 class="section-title hiw-title">How <b>It Works</b></h2>
    <p class="section-title hiw-sub">Lorem Ipsum is simply dummy text of the printing and typesetting industry.<br>Lorem Ipsum has been the industry's standard dummy text.</p>

    <svg class="abs" style="left:0;top:1480px" width="1200" height="100" aria-hidden="true">
      <path d="M290 25 C330 5 380 5 410 40 C440 80 480 80 508 42" fill="none" stroke="#2a4db0" stroke-width="1.5" stroke-dasharray="2 3"/>
      <path d="M502 40 L511 30 L510 44 Z" fill="#1d43b5"/>
      <path d="M672 62 C720 82 760 80 790 45 C820 5 865 5 890 50" fill="none" stroke="#2a4db0" stroke-width="1.5" stroke-dasharray="2 3"/>
      <path d="M884 52 L894 62 L894 48 Z" fill="#1d43b5"/>
    </svg>

    <div class="step-icon" style="left:184px;background:var(--blue)">
      <svg width="26" height="34" viewBox="0 0 26 34" aria-hidden="true"><rect x="3" y="1" width="20" height="32" rx="3" fill="none" stroke="#fff" stroke-width="2"/><rect x="7" y="7" width="12" height="16" fill="none" stroke="#fff" stroke-width="1.5"/><circle cx="13" cy="28" r="1.5" fill="#fff"/></svg>
    </div>
    <div class="step-icon" style="left:546px;background:#f22a0d">
      <svg width="34" height="34" viewBox="0 0 34 34" aria-hidden="true"><rect x="8" y="2" width="16" height="28" rx="3" fill="none" stroke="#fff" stroke-width="2"/><circle cx="24" cy="22" r="7" fill="#f22a0d" stroke="#fff" stroke-width="2"/><path d="M2 10 H8 M2 15 H8 M2 20 H8" stroke="#fff" stroke-width="1.5"/></svg>
    </div>
    <div class="step-icon" style="left:924px;background:var(--green)">
      <svg width="36" height="34" viewBox="0 0 36 34" aria-hidden="true"><rect x="2" y="2" width="14" height="9" rx="2" fill="none" stroke="#fff" stroke-width="1.5"/><rect x="18" y="8" width="16" height="11" fill="none" stroke="#fff" stroke-width="1.5"/><circle cx="12" cy="24" r="6" fill="none" stroke="#fff" stroke-width="2"/><circle cx="26" cy="26" r="4" fill="none" stroke="#fff" stroke-width="1.5"/></svg>
    </div>

    <h3 class="step-title" style="left:71px">Install the app</h3>
    <p class="step-text" style="left:71px">Get an exact quote for your exact<br>device and its condition.</p>
    <h3 class="step-title" style="left:433px">Bring</h3>
    <p class="step-text" style="left:433px">Bring your device into any one of our<br>convenient locations. We'll pull<br>up your quote right away.</p>
    <h3 class="step-title" style="left:761px;width:400px">Get Paid</h3>
    <p class="step-text" style="left:761px;width:400px">Get money as soon as we receive<br>your device. We'll review the condition</p>
  </section>

  <section class="about">
    <div class="about-art" role="img" aria-label="Illustration of a monitor holding a tablet and phone with a check mark"></div>
    <h2 class="about-title">About <b>Us</b></h2>
    <p class="about-copy">We are a leading company in the industry of computer and phone repairs throughout Florida. Cellport Depot is the place to go for an experienced, yet affordable cell phone and computer repair store!</p>
  </section>

  <footer class="footer">
    <div class="footer-brand"><span class="brand-dot"></span>TradeLoop</div>
    <nav class="footer-nav"><span>Home</span><span>Phones</span><span>Tablets</span><span>Contact</span></nav>
  </footer>
  <span class="social" style="left:515px" aria-label="Social link"></span>
  <span class="social active" style="left:560px" aria-label="Social link"></span>
  <span class="social" style="left:605px" aria-label="Social link"></span>
  <span class="social" style="left:650px" aria-label="Social link"></span>
  <p class="legal" style="left:160px">Copyright © 2021 TradeLoop</p>
  <p class="legal" style="left:873px">Terms of Use &nbsp;&nbsp;&nbsp;|&nbsp;&nbsp;&nbsp; Privacy Policy</p>

</div>
</body>
</html>
```